"Use it or Lose it" and "Brush on Over"

We are a dental office looking to connect with our patients through direct mail advertising. With the last 3 months of the year coming we would like to send out Post Cards to our patients letting them know they have 3 months left to "USE IT OR LOSE IT" when it comes to their dental insurance benefits.
So we are looking for a post card that has the "Use It or Lost it" theme along with our dental office logo, telephone number and address.

We are also looking for a post card that says "Brush On Over" to remind our patients that they are due for a dental cleaning and we would like for them to come over to our dental office for a well needed cleaning :).

```html
<!DOCTYPE html>
<html lang="en">
<head>
<meta charset="utf-8">
<title>Larkfield Dental – Brush-On Over Postcard</title>
<link rel="stylesheet" href="https://fonts.googleapis.com/css2?family=Montserrat:wght@300;400;800&family=Lato:wght@400&family=Cormorant+Garamond:wght@600&display=swap">
<style>
  :root {
    --backdrop: #d1d2d4;
    --paper: #ffffff;
    --ink: #000000;
    --brand-blue: #0e5a9c;
    --brand-blue-light: #2f8fd3;
    --rule-grey: #8a8a8a;
    --stamp-grey: #c6c5c6;
    --text-dark: #222222;
  }
  * { box-sizing: border-box; margin: 0; padding: 0; }
  html, body { width: 1200px; height: 1200px; overflow: hidden; }
  body { background: var(--backdrop); position: relative; font-family: "Montserrat", sans-serif; }

  .postcard {
    position: absolute; left: 172px; width: 856px; height: 544px;
    background: var(--paper); overflow: hidden;
    box-shadow: 4px 6px 8px rgba(0,0,0,0.18);
  }
  .postcard--front { top: 45px; }
  .postcard--back { top: 632px; }

  /* Front */
  .brand {
    position: absolute; left: 24px; top: 18px;
    display: flex; align-items: center; gap: 10px;
  }
  .brand__dot { width: 30px; height: 30px; border-radius: 50%; background: var(--brand-blue); }
  .brand__name {
    font-family: "Montserrat", sans-serif; font-weight: 400;
    color: var(--brand-blue); font-size: 24px; letter-spacing: 1px;
  }
  .headline {
    position: absolute; left: 32px; top: 160px;
    font-weight: 800; font-size: 84px; line-height: 84px; color: var(--ink);
    letter-spacing: -1px;
  }
  .headline__dots { display: inline-flex; gap: 25px; margin-left: 22px; vertical-align: baseline; }
  .headline__dots span {
    width: 19px; height: 19px; border-radius: 50%;
    background: radial-gradient(circle at 35% 35%, var(--brand-blue-light), var(--brand-blue));
  }
  .subhead {
    position: absolute; left: 36px; top: 333px;
    font-weight: 300; font-size: 18px; letter-spacing: 2px; color: var(--text-dark);
  }
  .toothbrush-art {
    position: absolute; left: 596px; top: 115px; width: 260px; height: 306px;
    background: linear-gradient(140deg, rgba(255,255,255,0) 20%, rgba(47,143,211,0.35) 55%, rgba(14,90,156,0.6) 100%);
  }
  .front-band {
    position: absolute; left: 0; bottom: 0; width: 100%; height: 123px;
    background: var(--ink); color: var(--paper);
    display: flex; align-items: center; justify-content: center; text-align: center;
    font-weight: 400; font-size: 20.5px; line-height: 26px; letter-spacing: 0.3px;
  }

  /* Back */
  .back-mark {
    position: absolute; left: 40px; top: 12px; width: 352px; height: 348px;
    display: flex; align-items: center; justify-content: center; gap: 14px;
  }
  .back-mark__dot { width: 44px; height: 44px; border-radius: 50%; background: var(--brand-blue); }
  .back-mark__name { font-family: "Montserrat", sans-serif; font-weight: 400; font-size: 34px; color: var(--brand-blue); }
  .divider { position: absolute; left: 431px; top: 8px; width: 2px; height: 352px; background: linear-gradient(var(--paper), #333 15%, #333 85%, var(--paper)); }
  .stamp { position: absolute; left: 692px; top: 16px; width: 104px; height: 118px; background: var(--stamp-grey); }
  .address-to { position: absolute; left: 494px; top: 156px; font-family: "Lato", sans-serif; font-size: 14px; color: var(--text-dark); }
  .address-line { position: absolute; left: 503px; width: 293px; height: 1px; background: var(--rule-grey); }

  .contact-row { position: absolute; display: flex; align-items: center; font-family: "Lato", sans-serif; font-size: 20px; }
  .contact-row .icon {
    width: 35px; height: 35px; border-radius: 50%;
    display: flex; align-items: center; justify-content: center; flex: none;
  }
  .contact-row--light { color: var(--text-dark); top: 379px; }
  .contact-row--light .icon { background: var(--brand-blue); }
  .contact-row--light .icon svg { fill: var(--paper); }
  .back-band { position: absolute; left: 0; bottom: 0; width: 100%; height: 117px; background: var(--ink); }
  .contact-row--dark { color: var(--paper); left: 21px; }
  .contact-row--dark .icon { background: var(--paper); width: 36px; height: 36px; }
  .contact-row--dark .icon svg { fill: var(--ink); }
  .contact-row--dark span { margin-left: 22px; }
</style>
</head>
<body>

<section class="postcard postcard--front">
  <div class="brand">
    <div class="brand__dot"></div>
    <div class="brand__name">LARKFIELD DENTAL</div>
  </div>
  <h1 class="headline">BRUSH-ON<br>OVER<span class="headline__dots"><span></span><span></span><span></span></span></h1>
  <p class="subhead">ITS CHECK-UP TIME</p>
  <div class="toothbrush-art" role="img" aria-label="Three blue toothbrushes with green, purple and red heads, angled across the corner"></div>
  <div class="front-band">GOOD DENTAL HABITS NEED TO BE FOSTERED AND<br>MAINTAINED EARLY RATHER THAN LATER.</div>
</section>

<section class="postcard postcard--back">
  <div class="back-mark">
    <div class="back-mark__dot"></div>
    <div class="back-mark__name">Larkfield Dental</div>
  </div>
  <div class="divider"></div>
  <div class="stamp"></div>
  <div class="address-to">To</div>
  <div class="address-line" style="top:223px"></div>
  <div class="address-line" style="top:266px"></div>
  <div class="address-line" style="top:307px"></div>

  <div class="contact-row contact-row--light" style="left:24px">
    <div class="icon"><svg width="20" height="20" viewBox="0 0 24 24"><path d="M12 2a10 10 0 1 0 0 20 10 10 0 0 0 0-20zm0 2c1 0 2.3 2 2.8 5H9.2C9.7 6 11 4 12 4zM4.3 11h3.4c0 .7 0 1.4.1 2H4.3a8 8 0 0 1 0-2zm.8 4h3c.3 1.6.8 3 1.5 4a8 8 0 0 1-4.5-4zm3-6h-3a8 8 0 0 1 4.5-4c-.7 1-1.2 2.4-1.5 4zm3.9 11c-1 0-2.3-2-2.8-5h5.6c-.5 3-1.8 5-2.8 5zm-3-7c0-.7 0-1.4.1-2h5.8c.1.6.1 1.3.1 2s0 1.4-.1 2H9.1c-.1-.6-.1-1.3-.1-2zm5.4 6c.7-1 1.2-2.4 1.5-4h3a8 8 0 0 1-4.5 4zm1.8-6c.1-.6.1-1.3.1-2s0-1.4-.1-2h3.4a8 8 0 0 1 0 4h-3.4zm-.3-6c-.3-1.6-.8-3-1.5-4a8 8 0 0 1 4.5 4h-3z"/></svg></div>
    <span style="margin-left:34px">larkfielddental.com</span>
  </div>
  <div class="contact-row contact-row--light" style="left:327px">
    <div class="icon"><svg width="18" height="18" viewBox="0 0 24 24"><path d="M7 3h8v5H7zM3 9h18v11H3zm3 3v2h4v-2zm0 3v2h4v-2zm6-3v2h2v-2zm3 0v2h2v-2zm-3 3v2h2v-2zm3 0v2h2v-2z"/></svg></div>
    <span style="margin-left:20px">555 - 210 - 4683</span>
  </div>
  <div class="contact-row contact-row--light" style="left:581px; top:382px">
    <div class="icon"><svg width="17" height="17" viewBox="0 0 24 24"><path d="M6.6 10.8a15 15 0 0 0 6.6 6.6l2.2-2.2c.3-.3.7-.4 1-.2 1.1.4 2.3.6 3.6.6.6 0 1 .4 1 1V20c0 .6-.4 1-1 1A17 17 0 0 1 3 4c0-.6.4-1 1-1h3.5c.6 0 1 .4 1 1 0 1.3.2 2.5.6 3.6.1.3 0 .7-.2 1z"/></svg></div>
    <span style="margin-left:20px">555 - 210 - 4690</span>
  </div>

  <div class="back-band">
    <div class="contact-row contact-row--dark" style="top:16px">
      <div class="icon"><svg width="18" height="18" viewBox="0 0 24 24"><path d="M12 2a7 7 0 0 0-7 7c0 5 7 13 7 13s7-8 7-13a7 7 0 0 0-7-7zm0 9.5A2.5 2.5 0 1 1 12 6.5a2.5 2.5 0 0 1 0 5z"/></svg></div>
      <span>72 Maple Row Larkfield, NJ 07000</span>
    </div>
    <div class="contact-row contact-row--dark" style="top:66px">
      <div class="icon"><svg width="18" height="18" viewBox="0 0 24 24"><path d="M3 5h18v14H3zm2 2v.5l7 5 7-5V7l-7 5z"/></svg></div>
      <span>hello@larkfielddental.com</span>
    </div>
  </div>
</section>

</body>
</html>
```